Workshop PPT Update for AI Transformation Sessions

Our strategic consulting firm runs strategy workshops using slides as workshop exercises. These slides are used to communicate to the participants in advance, run the workshops and produce the final deliverable.

It is time for a design "upgrade". We'd like them to be more engaging, hipper and more interesting. These slides are utilitarian, so clean and usable is good. I have attached the example of what we have today. I have also attached an example of another company's slides that I like.

We can't rip off their design nor can we go away 100% from what we have. But I think it is possible to "update" our look to something closer to their look. Grey colors are fine with some color pop.

Slide styles needed are - 1) Cover Page, 2) Instructions Page, 3) Bullet list 4) Worksheet (place for participants to add content 5) Table, 6) Two column.

```html
<!DOCTYPE html>
<html lang="en">
<head>
<meta charset="utf-8">
<title>AI Transformation Workshop Slides</title>
<link href="https://fonts.googleapis.com/css2?family=Poppins:wght@600;700&family=Roboto:wght@400;500;700&display=swap" rel="stylesheet">
<style>
:root{
  --canvas:#8f8f8f;
  --paper:#ffffff;
  --red:#a8403f;
  --red-ring:#e9cfce;
  --ink:#232131;
  --muted:#6b6b6b;
  --cover:#2d2540;
  --row:#f2f6fb;
}
*{box-sizing:border-box;margin:0;padding:0}
html,body{width:1200px;height:1092px;overflow:hidden}
body{background:var(--canvas);font-family:"Roboto",Arial,sans-serif;color:var(--ink);position:relative}
.slide{position:absolute;width:541px;height:305px;background:var(--paper);overflow:hidden}
.s-getting{left:40px;top:52px}
.s-creating{left:618px;top:52px}
.s-cover{left:40px;top:398px;background:var(--cover)}
.s-principles{left:618px;top:398px}
.s-workshop{left:40px;top:735px}
.s-plan{left:618px;top:735px}

.slide-title{position:absolute;left:25px;top:12px;height:22px;padding-left:12px;border-left:3px solid var(--red);font-family:"Poppins",sans-serif;font-weight:700;font-size:18px;line-height:22px;color:var(--ink)}
.brand{position:absolute;right:25px;top:9px;font-family:"Roboto",sans-serif;font-weight:400;font-size:14px;color:var(--ink);display:flex;align-items:center;gap:4px}
.brand .dot{width:8px;height:8px;border-radius:50%;background:var(--red)}
.s-cover .brand{color:#fff}

.footer{position:absolute;left:0;right:0;bottom:0;height:14px;background:var(--red);color:#fff;font-size:4.5px;display:flex;justify-content:space-between;align-items:center;padding:0 24px}

.icon{width:37px;height:37px;border-radius:50%;background:var(--red);box-shadow:0 0 0 2px var(--red-ring);display:flex;align-items:center;justify-content:center;flex:none}
.icon svg{width:20px;height:20px;fill:none;stroke:#fff;stroke-width:1.4;stroke-linecap:round;stroke-linejoin:round}

.photo{position:absolute;left:270px;top:40px;width:271px;height:232px;border-radius:12px 0 0 12px}
.photo-meeting{background:linear-gradient(135deg,#d8d5d0 0%,#a48b76 45%,#5b4a40 100%)}
.photo-team{background:linear-gradient(135deg,#e6e6e4 0%,#b7b2ad 50%,#4e4a48 100%)}

.steps{position:absolute;left:25px;top:68px;list-style:none}
.steps li{display:flex;align-items:center;gap:10px;height:37px;margin-bottom:9.5px;font-size:8px;font-weight:700}

.meta{position:absolute;left:24px;display:flex;font-size:9.5px;font-weight:500}
.meta .k{display:flex;align-items:flex-start;gap:4px}
.meta small{font-size:7px;font-weight:400;color:var(--muted)}
.meta i{display:inline-block;width:8px;height:8px;border-radius:2px;background:var(--red);margin-top:2px;flex:none}

.grid3{position:absolute;left:10px;right:10px;display:grid;grid-template-columns:repeat(3,1fr);row-gap:8px}
.grid3 .cell{display:flex;flex-direction:column;align-items:center;text-align:center}
.grid3 .icon{margin-bottom:10px}
.grid3 h4{font-size:7px;font-weight:500}
.grid3 p{font-size:5.2px;color:var(--muted);margin-top:3px;line-height:1.5;max-width:130px}

.cover-photo{position:absolute;right:0;top:0;width:330px;height:305px;background:radial-gradient(ellipse at 70% 45%,#8a7770 0%,#514356 40%,rgba(45,37,64,0) 75%)}
.cover-title{position:absolute;left:24px;top:121px;font-family:"Poppins",sans-serif;font-weight:700;font-size:27px;color:#fff}
.cover-sub{position:absolute;left:24px;top:163px;font-size:11.5px;font-weight:500;color:#fff}

.principles{position:absolute;left:25px;top:49px;list-style:none;width:240px}
.principles li{display:flex;gap:10px;height:48px}
.principles h4{font-size:8px;font-weight:500;margin-top:3px}
.principles p{font-size:5.8px;color:var(--muted);line-height:1.55;margin-top:4px;white-space:nowrap}

.plan-table{position:absolute;left:24px;top:85px;width:493px;border-collapse:collapse;font-size:6px;font-weight:700;text-align:center}
.plan-table th{background:var(--red);color:#fff;font-weight:500;font-size:9px;height:19px;border-right:1px solid #fff}
.plan-table td{background:var(--row);height:29px;border-right:1px solid #fff;border-bottom:1px solid #fff}
.plan-table td.num{font-size:8px}
.plan-table td small{font-weight:400;font-size:4.8px}
</style>
</head>
<body>

<svg width="0" height="0" style="position:absolute" aria-hidden="true">
  <symbol id="i-doc" viewBox="0 0 20 20"><rect x="4" y="2.5" width="12" height="15" rx="1.5"/><path d="M7 7h6M7 10h6M7 13h4"/></symbol>
  <symbol id="i-pen" viewBox="0 0 20 20"><path d="M4 16l1-4 9-9 3 3-9 9z M12 5l3 3"/></symbol>
  <symbol id="i-people" viewBox="0 0 20 20"><circle cx="7" cy="7" r="2.5"/><circle cx="13" cy="7" r="2.5"/><path d="M3 16c0-3 2-5 4-5s4 2 4 5M9 16c0-3 2-5 4-5s4 2 4 5"/></symbol>
  <symbol id="i-mail" viewBox="0 0 20 20"><rect x="3" y="5" width="14" height="11" rx="1"/><path d="M3 6l7 5 7-5"/></symbol>
  <symbol id="i-search" viewBox="0 0 20 20"><circle cx="9" cy="9" r="4.5"/><path d="M12.5 12.5l4 4"/></symbol>
  <symbol id="i-check" viewBox="0 0 20 20"><rect x="4" y="2.5" width="11" height="15" rx="1.5"/><path d="M7 7h5M7 10h3"/><circle cx="14" cy="14" r="3"/><path d="M12.8 14l1 1 1.6-1.8"/></symbol>
  <symbol id="i-globe" viewBox="0 0 20 20"><circle cx="10" cy="10" r="6.5"/><path d="M3.5 10h13M10 3.5c3 3 3 10 0 13M10 3.5c-3 3-3 10 0 13"/></symbol>
  <symbol id="i-gear" viewBox="0 0 20 20"><circle cx="10" cy="10" r="3"/><path d="M10 3v2M10 15v2M3 10h2M15 10h2M5 5l1.4 1.4M13.6 13.6L15 15M5 15l1.4-1.4M13.6 6.4L15 5"/></symbol>
  <symbol id="i-hand" viewBox="0 0 20 20"><path d="M3 14h4l4 2 6-3-1-1-4 1H9M3 14v-3h4l3 1"/><circle cx="12" cy="6" r="2.5"/></symbol>
</svg>

<!-- Getting Started -->
<section class="slide s-getting">
  <h2 class="slide-title">Getting Started</h2>
  <div class="brand"><span class="dot"></span>NorthPath</div>
  <ul class="steps">
    <li><span class="icon"><svg><use href="#i-check"/></svg></span>Complete the Engagement Sizing Survey.</li>
    <li><span class="icon"><svg><use href="#i-doc"/></svg></span>Collect relevant inputs.</li>
    <li><span class="icon"><svg><use href="#i-people"/></svg></span>Determine workshop participants &amp; date.</li>
    <li><span class="icon"><svg><use href="#i-mail"/></svg></span>Send invites, to include pre-work.</li>
  </ul>
  <div class="photo photo-meeting" role="img" aria-label="Photo of a team meeting around a table with laptops and papers"></div>
  <footer class="footer"><span>Page No:01</span><span>Copyright © 2024 NorthPath. All Rights Reserved.</span></footer>
</section>

<!-- Creating your AI Guiding Principles -->
<section class="slide s-creating">
  <h2 class="slide-title">Creating your AI Guiding Principles</h2>
  <div class="brand"><span class="dot"></span>NorthPath</div>
  <div class="meta" style="top:65px;gap:20px">
    <div>
      <div class="k"><i></i>AskMate Prompts HERE: <small style="margin-top:2px">Execs</small></div>
      <div class="k" style="margin-top:8px"><i></i>Examples for Inspiration: <small style="margin-top:2px">See next slides</small></div>
    </div>
    <div class="k" style="width:290px"><i></i><span>Your Existing Material: <small>Company Values,Current Policies (GDPR, CCPA, etc.), Legal Guidance,OTHER.</small></span></div>
  </div>
  <div class="grid3" style="top:121px">
    <div class="cell"><span class="icon"><svg><use href="#i-pen"/></svg></span><h4>Create the Outline</h4><p>Determine the topics that need a principle.</p></div>
    <div class="cell"><span class="icon"><svg><use href="#i-doc"/></svg></span><h4>Draft the Guiding Principles</h4></div>
    <div class="cell"><span class="icon"><svg><use href="#i-search"/></svg></span><h4>Audit the Outline</h4><p>Look at the current policies to determine if all topics are covered.</p></div>
    <div class="cell"><span class="icon"><svg><use href="#i-check"/></svg></span><h4>Determine which GPs need detailed policies.</h4></div>
    <div class="cell"><span class="icon"><svg><use href="#i-hand"/></svg></span><h4>Determine which AI Tools support the GPs</h4></div>
    <div class="cell"><span class="icon"><svg><use href="#i-doc"/></svg></span><h4>Finalize via a legal and executive review</h4></div>
  </div>
  <footer class="footer"><span>Page No:04</span><span>Copyright © 2024 NorthPath. All Rights Reserved.</span></footer>
</section>

<!-- Cover -->
<section class="slide s-cover">
  <div class="cover-photo" role="img" aria-label="Darkened photo of a businessman working at a laptop"></div>
  <div class="brand"><span class="dot"></span>NorthPath</div>
  <h1 class="cover-title">Kickoff &amp; Discovery</h1>
  <p class="cover-sub">Sizing &amp; Scoping AI Transformation</p>
</section>

<!-- AI Guiding Principles -->
<section class="slide s-principles">
  <h2 class="slide-title">AI Guiding Principles</h2>
  <div class="brand"><span class="dot"></span>NorthPath</div>
  <ul class="principles">
    <li><span class="icon"><svg><use href="#i-check"/></svg></span><div><h4>Principle 01</h4><p>Complete perspective from Executives, Directors, Managers &amp; Staff.<br>Conduct competitive analysis and customer research (optional).</p></div></li>
    <li><span class="icon"><svg><use href="#i-check"/></svg></span><div><h4>Principle 02</h4><p>Complete perspective from Executives, Directors, Managers &amp; Staff.<br>Conduct competitive analysis and customer research (optional).</p></div></li>
    <li><span class="icon"><svg><use href="#i-check"/></svg></span><div><h4>Principle 03</h4><p>Complete perspective from Executives, Directors, Managers &amp; Staff.<br>Conduct competitive analysis and customer research (optional).</p></div></li>
    <li><span class="icon"><svg><use href="#i-check"/></svg></span><div><h4>Principle 04</h4><p>Complete perspective from Executives, Directors, Managers &amp; Staff.<br>Conduct competitive analysis and customer research (optional).</p></div></li>
    <li><span class="icon"><svg><use href="#i-check"/></svg></span><div><h4>Principle 05</h4><p>Complete perspective from Executives, Directors, Managers &amp; Staff.<br>Conduct competitive analysis and customer research (optional).</p></div></li>
  </ul>
  <div class="photo photo-team" role="img" aria-label="Photo of colleagues leaning over a desk reviewing documents"></div>
  <footer class="footer"><span>Page No:05</span><span>Copyright © 2024 NorthPath. All Rights Reserved.</span></footer>
</section>

<!-- Workshop Overview -->
<section class="slide s-workshop">
  <h2 class="slide-title">Workshop Overview</h2>
  <div class="brand"><span class="dot"></span>NorthPath</div>
  <div class="meta" style="top:65px;gap:26px">
    <div class="k"><i></i>Participants: <small style="margin-top:2px">Execs</small></div>
    <div class="k"><i></i>Duration: <small style="margin-top:2px">2 hrs</small></div>
    <div class="k" style="width:245px"><i></i><span>Prep Work: <small>Org Strategy,2023 Goal Performance,Existing policies, Pre-thinking questions.</small></span></div>
  </div>
  <div class="grid3" style="top:108px">
    <div class="cell"><span class="icon"><svg><use href="#i-check"/></svg></span><h4>Confirm Company Direction</h4><p>Recap organizational purpose, values, vision &amp; winning strategy.</p></div>
    <div class="cell"><span class="icon"><svg><use href="#i-gear"/></svg></span><h4>Develop AI Vision</h4></div>
    <div class="cell"><span class="icon"><svg><use href="#i-people"/></svg></span><h4>Develop AI Guiding Principles</h4><p>Developed AI Guiding Principles, supporting policies to include approved tools.</p></div>
    <div class="cell"><span class="icon"><svg><use href="#i-hand"/></svg></span><h4>Agree on a Governance Approach</h4><p>Agreed upon governance approach, structure, &amp; executive champion.</p></div>
    <div class="cell"><span class="icon"><svg><use href="#i-gear"/></svg></span><h4>Agree on a Training &amp; Learning Approach</h4><p>Set approach to training &amp; continuous learning.</p></div>
    <div class="cell"><span class="icon"><svg><use href="#i-globe"/></svg></span><h4>Determine Rollout &amp; Communication</h4><p>Organizational rollout &amp; continuous communication.</p></div>
  </div>
  <footer class="footer"><span>Page No:03</span><span>Copyright © 2024 NorthPath. All Rights Reserved.</span></footer>
</section>

<!-- Plan Structure -->
<section class="slide s-plan">
  <h2 class="slide-title">Plan Structure</h2>
  <div class="brand"><span class="dot"></span>NorthPath</div>
  <table class="plan-table">
    <colgroup><col style="width:34px"><col style="width:33px"><col style="width:173px"><col style="width:127px"><col style="width:126px"></colgroup>
    <thead><tr><th colspan="2">Level</th><th>Planning Element &amp; Definition</th><th>Accountability/Owner</th><th>Frequency of Modification</th></tr></thead>
    <tbody>
      <tr><td class="num">1</td><td>What<br><small>(overall)</small></td><td>Strategic Priorities</td><td>N/A</td><td>3+ years</td></tr>
      <tr><td class="num">1.1</td><td>What<br><small>(This Year)</small></td><td>Goals <small>(Outcomes &amp; Strategies)</small></td><td>Executive Leadership</td><td>1-3 years</td></tr>
      <tr><td class="num">1.1.1</td><td rowspan="2">How</td><td>Key Performance Indicators and/or Initiatives</td><td></td><td>1 year <small>(w/ qrtly targets)</small></td></tr>
      <tr><td class="num">1.1.1.1</td><td>Action Items</td><td></td><td>Quarterly/Monthly</td></tr>
    </tbody>
  </table>
  <footer class="footer"><span>Page No:06</span><span>Copyright © 2024 NorthPath. All Rights Reserved.</span></footer>
</section>

</body>
</html>
```